Larkmoor Leisure Group (LLG)

We need a business card design for Larkmoor Leisure Group. Modern and sleek looking, with all critical information. Open to single or double sided designs, if double sided info needs to be all on one side. The main Logo is Larkmoor Leisure group and must be on the card. The other three logos are for the brands that fall under the group, they might be good on the back.

Industry/Entity Type

Business

```html
<!DOCTYPE html>
<html lang="en">
<head>
<meta charset="utf-8">
<title>Larkmoor Leisure Group – Business Card</title>
<link rel="stylesheet" href="https://fonts.googleapis.com/css2?family=Lato:wght@400;700&family=Montserrat:wght@500;600&display=swap">
<style>
  :root {
    --backdrop: #353535;
    --card-white: #ffffff;
    --band-grey: #ececee;
    --brand-blue: #1f4e9c;
    --brand-green: #7a9a2a;
    --ink: #1e1e1e;
    --muted: #555a60;
  }
  * { margin: 0; padding: 0; box-sizing: border-box; }
  html, body { width: 1200px; height: 900px; overflow: hidden; }
  body { background: var(--backdrop); position: relative; font-family: "Lato", sans-serif; }

  .card {
    position: absolute; top: 306px; width: 439px; height: 271px;
    border-radius: 10px; overflow: hidden;
    box-shadow: 2px 3px 6px rgba(0,0,0,.45);
  }
  .card-front { left: 149px; background: var(--card-white); }
  .card-back {
    left: 608px;
    background: linear-gradient(150deg, #8da53a 0%, #3f6fa0 32%, #1f55a0 50%, #3f6fa0 68%, #8da53a 100%);
  }

  /* Front: identity */
  .group-identity {
    position: absolute; left: 20px; top: 78px; width: 200px; text-align: center;
    font-family: "Montserrat", sans-serif; font-weight: 600; color: var(--brand-blue);
  }
  .group-mark {
    display: block; width: 40px; height: 40px; margin: 0 auto 14px;
    background: var(--brand-blue); border-radius: 4px;
  }
  .group-name { font-size: 14px; letter-spacing: .3px; line-height: 1.1; }
  .group-sub {
    display: flex; align-items: center; gap: 8px; margin-top: 4px;
    font-size: 13px; letter-spacing: 5px;
  }
  .group-sub::before, .group-sub::after {
    content: ""; flex: 1; height: 1.5px; background: var(--brand-blue);
  }

  .divider { position: absolute; left: 238px; top: 54px; width: 1px; height: 138px; background: var(--brand-blue); }

  .contact { position: absolute; left: 257px; top: 52px; color: var(--ink); }
  .person-name { font-size: 16px; letter-spacing: .3px; color: var(--brand-blue); line-height: 1.15; }
  .person-name .surname { color: var(--brand-green); }
  .person-role { font-size: 12px; margin-bottom: 9px; }
  .contact-list { list-style: none; font-size: 12px; line-height: 16px; }
  .contact-list li { display: flex; align-items: center; gap: 6px; }
  .contact-list svg { width: 9px; height: 9px; fill: var(--brand-blue); flex: none; }
  .address { font-size: 12px; line-height: 16px; margin-top: 6px; }

  .brand-band {
    position: absolute; left: 0; bottom: 0; width: 100%; height: 68px;
    background: var(--band-grey);
    display: flex; align-items: center; justify-content: space-around; padding: 0 18px;
  }
  .brand-name {
    display: flex; align-items: center; gap: 5px;
    font-weight: 700; font-size: 13px; color: var(--brand-blue);
  }
  .brand-name .dot { width: 14px; height: 14px; border-radius: 50%; background: var(--brand-blue); }

  /* Back */
  .back-pattern { position: absolute; inset: 0; }
  .back-monogram {
    position: absolute; left: 300px; top: 152px;
    font-family: "Montserrat", sans-serif; font-weight: 600; font-size: 22px;
    color: var(--card-white); letter-spacing: 1px;
  }
</style>
</head>
<body>
  <section class="card card-front">
    <div class="group-identity">
      <span class="group-mark"></span>
      <div class="group-name">LARKMOOR LEISURE</div>
      <div class="group-sub">GROUP</div>
    </div>

    <div class="divider"></div>

    <div class="contact">
      <div class="person-name">DANIEL <span class="surname">WHITCOMBE</span></div>
      <div class="person-role">Managing Director</div>
      <ul class="contact-list">
        <li><svg viewBox="0 0 10 10"><path d="M1 3q4-3 8 0v1.5H7V3.6Q5 3 3 3.6V4.5H1zM2 5h6l1 4H1z"/></svg>055-210 334 876</li>
        <li><svg viewBox="0 0 10 10"><path d="M2.5 0h5v10h-5zM3.3 1v7h3.4V1z"/></svg>055-210 334 876</li>
        <li><svg viewBox="0 0 10 10"><path d="M0 2h10v6H0zM1 3l4 3 4-3z"/></svg>hello@larkmoorleisure.com</li>
        <li><svg viewBox="0 0 10 10"><circle cx="5" cy="5" r="5"/></svg>www.larkmoorleisure.com</li>
      </ul>
      <div class="address">12345, Address Goes Here<br>Country Name, 123456.</div>
    </div>

    <div class="brand-band">
      <span class="brand-name">Standhall Hospitality</span>
      <span class="brand-name">HarbourTickets</span>
      <span class="brand-name"><span class="dot"></span>seatmark</span>
    </div>
  </section>

  <section class="card card-back">
    <div class="back-pattern" role="img" aria-label="Faint repeating pattern of the group's hexagon mark over a green-to-blue gradient"></div>
    <div class="back-monogram">LLG</div>
  </section>
</body>
</html>
```